Powerpoint Design for business and consulting company - Dorneck-Saalig

I am searching a design specialist who can help me to create a PowerPoint Design for my company. I'm in the business coaching and consulting industry.

The PPT master should be easy to use and include professional formatting (using the fonts of my website). In general, the slide master should have the look and feel of my website (in terms of fonts, colors, logos, possibility to place big photographs, having text and graph slides as well as photo slides with just 1 key message).

The PowerPoint design should fit my cooperate Identity (please see my website https://dorneck-saalig.de).
My logos are attached.

Additional information:
- wide screen format - 16: 9
- right set up of a fitting color scheme
https: // farbwexo. io / f6ded1-bfcbce-807f84-9cd3d1-666666
# 666666 (Dim Gray) - body / heading text
# 807F84 (Gray Web)
#BFCBCE (Silver Sand) - link hover
# 9cd3d1 (Powder Blue) - Link color
# F6DED1 (Champagne Pink)

- creation of chart templates, using chart tools, and different chart types etc.
- creation of different slide layouts to place content, pictures (in different sizes), optionally Media
- set up of display guide lines
- as well as standard elements, such as text boxes, lines, default shapes, etc.

Requirements
Must have
• Powerpoint Design needs to have:
https://farbwexo.io/f6ded1-bfcbce-807f84-9cd3d1-666666
# 807F84 (Gray Web)
# F6DED1 (Champagne Pink)

```html
<!DOCTYPE html>
<html lang="en">
<head>
<meta charset="utf-8">
<title>Dorneck-Saalig – Presentation Master</title>
<link rel="stylesheet" href="https://fonts.googleapis.com/css2?family=Roboto:wght@300;400;500;700;900&display=swap">
<style>
:root{
  --teal:#9cd3d1;--teal-dark:#86c4c2;--pink:#f6ded1;--silver:#bfcbce;--gray:#807f84;--text:#666666;
  --ink:#3c3c3c;--paper:#ffffff;--mist:#f6f7f7;--frame:#595959;
}
*{box-sizing:border-box;margin:0;padding:0}
html,body{width:1200px;height:2501px;overflow:hidden;background:var(--frame);font-family:"Roboto",sans-serif;color:var(--text)}
.deck{display:grid;grid-template-columns:repeat(3,396px);grid-auto-rows:223px;gap:4px;padding:4px 2px;width:1200px;height:2501px}
.slide{position:relative;overflow:hidden;background:var(--paper)}
.slide.mist{background:var(--mist)}
.a{position:absolute}
svg.fill{position:absolute;inset:0;width:100%;height:100%}
.brand{position:absolute;font-weight:500;font-size:10px;letter-spacing:.2px;color:#fff;white-space:nowrap}
.brand.sm{font-size:7px;color:var(--ink);left:10px;bottom:5px}
.page{position:absolute;right:12px;bottom:6px;font-size:3.5px;letter-spacing:1px;color:var(--gray)}
.t{font-size:4.2px;line-height:1.4;color:var(--gray)}
.h{font-weight:500;color:var(--text)}
.white{color:#fff}
.accent-line{position:absolute;left:14px;top:12px;width:1px;height:22px;background:var(--pink)}
/* photo placeholders */
.ph-desk{background:linear-gradient(135deg,#7a5a44,#3b2b22 55%,#2d3f5c)}
.ph-steps{background:linear-gradient(160deg,#b9bcbd,#8e9598 60%,#6d7377)}
.ph-lightbox{background:radial-gradient(ellipse at 50% 30%,#e9ecea 0 18%,#23303a 45%,#0f1820)}
.ph-mountain{background:linear-gradient(180deg,#9cc0dc,#dfe8ee 40%,#6f7d6a 60%,#3e4a3a)}
.ph-forest{background:linear-gradient(180deg,#2f4a36,#486048 50%,#8a6e5c 80%,#6a5446)}
.ph-portrait{background:linear-gradient(180deg,#d6d6d6,#9a9a9a)}
.ph-waterfall{background:linear-gradient(180deg,#2e4b3c,#7f9a8c 45%,#3a5646)}
.ph-tower{background:linear-gradient(180deg,#c9cccd,#e3e5e6 40%,#a4a8aa)}
.ph-street{background:linear-gradient(120deg,#3b3430,#8e6a4b 50%,#f1b36b 70%,#3c3634)}
.ph-sticky{background:linear-gradient(135deg,#f3f1ee,#f7c873 40%,#ef9aa9 60%,#ede8e1)}
.ph-office{background:linear-gradient(180deg,#545a5d,#a1a6a8 60%,#6b7174)}
.ph-compass{background:linear-gradient(180deg,#a8c4d8,#c2a97a 60%,#6f5b3e)}
.ph-laptop{background:linear-gradient(135deg,#d9d2c7,#8f8a86 60%,#5c5856)}
.ph-meeting{background:linear-gradient(135deg,#c9c6c0,#e7e3dc 50%,#9b948b)}
.ph-table{background:linear-gradient(135deg,#2a1f1a,#6b4a35 50%,#2e3f5a)}
/* agenda */
.agenda-panel{position:absolute;left:0;top:0;width:150px;height:100%}
.agenda-title{position:absolute;left:36px;top:104px;font-size:15px;font-weight:500;color:#fff;letter-spacing:.5px}
.agenda-list{position:absolute;left:134px;top:56px;width:200px;list-style:none}
.agenda-list li{display:flex;height:15.3px;align-items:center;border-bottom:.5px solid #ccc;font-size:6px;color:var(--ink)}
.agenda-list li span{width:26px;color:var(--gray);font-size:5.5px}
/* icons */
.dot{position:absolute;border-radius:50%;display:flex;align-items:center;justify-content:center}
.bullet-row{position:absolute;display:flex;gap:5px}
.bullet-row i{flex:none;width:7px;height:7px;border-radius:50%;border:1px solid var(--pink)}
.card{position:absolute;background:#fff;box-shadow:0 1px 4px rgba(0,0,0,.08)}
.stat-circle{position:absolute;width:76px;height:76px;border-radius:50%;border:4px solid #fff;box-shadow:0 0 0 1px #eee;color:#fff;text-align:center;padding-top:14px}
.stat-circle b{display:block;font-size:18px;font-weight:700}
.stat-circle span{display:block;font-size:3.6px;line-height:1.4;padding:2px 10px 0;opacity:.9}
.contact{display:flex;align-items:center;gap:8px;font-size:5px}
</style>
</head>
<body>
<main class="deck">

<!-- 1 title left -->
<section class="slide">
  <div class="a ph-desk" style="inset:0" role="img" aria-label="Photo of a wooden desk with a laptop, notebook and coffee"></div>
  <svg class="fill" viewBox="0 0 396 223" preserveAspectRatio="none"><path d="M0 0H282C238 40 232 150 300 223H0Z" fill="#c8d0d2"/></svg>
  <div class="a" style="left:22px;top:82px;width:1.5px;height:45px;background:var(--pink)"></div>
  <div class="a white" style="left:32px;top:84px;font-size:15px;line-height:1.35"><div style="font-weight:500">Your title goes here</div><div style="font-weight:300">One-two sentences</div></div>
  <div class="brand" style="left:30px;top:192px">dorneck-saalig</div>
</section>

<!-- 2 title right -->
<section class="slide">
  <div class="a ph-steps" style="inset:0" role="img" aria-label="Photo of a smiling coach seated on outdoor steps"></div>
  <svg class="fill" viewBox="0 0 396 223" preserveAspectRatio="none"><path d="M396 0H282C214 50 196 160 250 223H396Z" fill="var(--teal)"/></svg>
  <div class="a" style="right:10px;top:86px;width:1.5px;height:46px;background:#fff"></div>
  <div class="a white" style="right:18px;top:88px;font-size:15px;line-height:1.35;text-align:right"><div style="font-weight:500">Your title goes here</div><div style="font-weight:300">One-two sentences</div></div>
  <div class="brand" style="left:276px;top:194px">dorneck-saalig</div>
</section>

<!-- 3 lightbox -->
<section class="slide" style="background:var(--teal)">
  <div class="a ph-lightbox" style="left:0;top:0;width:330px;height:190px;border-bottom-right-radius:100% 100%" role="img" aria-label="Photo of a lightbox sign reading think outside the box"></div>
  <svg class="fill" viewBox="0 0 396 223" preserveAspectRatio="none"><path d="M0 175C120 176 240 130 300 0H396V223H0Z" fill="var(--teal)"/><path d="M0 0H80C40 10 10 40 0 70Z" fill="#b9e0de"/></svg>
  <div class="a white" style="right:28px;top:188px;font-size:9px;font-weight:700;letter-spacing:1.6px">ADD YOUR TEXT HERE</div>
  <div class="brand" style="left:16px;top:192px">dorneck-saalig</div>
</section>

<!-- 4 agenda teal -->
<section class="slide">
  <div class="agenda-panel" style="background:var(--teal)"></div>
  <div class="agenda-title">AGENDA</div>
  <ol class="agenda-list">
    <li><span>01</span>Introduction - Welcome</li><li><span>02</span>Mission &amp; Vision</li><li><span>03</span>Our Services</li><li><span>04</span>Company Profile</li><li><span>05</span>Project Portfolio</li><li><span>06</span>Our Team</li><li><span>07</span>Our Offices</li><li><span>08</span>Q&amp;As / Closing Speech</li>
  </ol>
  <div class="brand" style="left:30px;top:192px">dorneck-saalig</div>
  <div class="page">PAGE | 6</div>
</section>

<!-- 5 agenda photo -->
<section class="slide">
  <div class="agenda-panel ph-tower" style="background:linear-gradient(160deg,#c9cfd1,#8f989b)" role="img" aria-label="Muted photo of a modern office tower"></div>
  <div class="agenda-title" style="left:44px">AGENDA</div>
  <ol class="agenda-list" style="left:145px">
    <li><span>01</span>Introduction - Welcome</li><li><span>02</span>Mission &amp; Vision</li><li><span>03</span>Our Services</li><li><span>04</span>Company Profile</li><li><span>05</span>Project Portfolio</li><li><span>06</span>Our Team</li><li><span>07</span>Our Offices</li><li><span>08</span>Q&amp;As / Closing Speech</li>
  </ol>
  <div class="brand" style="left:30px;top:192px">dorneck-saalig</div>
  <div class="page">PAGE | 7</div>
</section>

<!-- 6 quote -->
<section class="slide">
  <div class="dot" style="left:190px;top:128px;width:16px;height:16px;background:var(--teal);color:#fff;font-size:11px;font-weight:900;line-height:1">“</div>
  <p class="a" style="left:70px;top:152px;width:256px;text-align:center;font-size:6px;line-height:1.35;color:var(--ink)">Lorem ipsum dolor sit amet, consectetur adipiscing elit. Lorem ipsum dolor sit amet, consectetur adipiscing elit, sed do eiusmod tempor incididunt ut labore et dolore magna aliqua.</p>
  <div class="a h" style="left:0;right:0;top:189px;text-align:center;font-size:5.5px">Your Name</div>
</section>

<!-- 7 quote photo -->
<section class="slide">
  <div class="a ph-mountain" style="inset:0" role="img" aria-label="Photo of a hiker standing on a rock above a mountain valley"></div>
  <svg class="fill" viewBox="0 0 396 223" preserveAspectRatio="none"><path d="M0 170C130 166 270 178 396 168V223H0Z" fill="var(--teal)"/></svg>
  <div class="dot" style="left:24px;top:181px;width:15px;height:15px;border:1px solid #fff;color:#fff;font-size:10px;font-weight:900">“</div>
  <p class="a white" style="left:44px;top:180px;width:340px;text-align:center;font-size:5.5px;line-height:1.35">Lorem ipsum dolor sit amet, consectetur adipiscing elit. Lorem ipsum dolor sit amet, consectetur adipiscing elit, sed do eiusmod tempor incididunt ut labore et dolore magna aliqua.</p>
  <div class="a h" style="left:0;right:0;top:206px;text-align:center;font-size:5.5px;color:var(--ink)">Your Name</div>
</section>

<!-- 8 section divider pill -->
<section class="slide">
  <div class="a ph-forest" style="inset:0" role="img" aria-label="Photo of a woman walking across a wooden bridge in a forest"></div>
  <div class="a" style="left:100px;top:155px;width:170px;height:36px;border-radius:18px;background:rgba(200,210,212,.75)"></div>
  <div class="dot" style="left:105px;top:164px;width:19px;height:19px;background:var(--teal)"><svg width="10" height="10" viewBox="0 0 10 10"><circle cx="5" cy="5" r="4" fill="none" stroke="#fff" stroke-width="1"/><circle cx="5" cy="5" r="1.5" fill="#fff"/></svg></div>
  <div class="a white" style="left:128px;top:163px;font-size:13px;font-weight:300;line-height:1">SECTION DIVIDER</div>
  <div class="a white" style="left:128px;top:177px;font-size:6px">SECTION SUBTITLE</div>
</section>

<!-- 9 section divider band -->
<section class="slide">
  <div class="a ph-forest" style="inset:0" role="img" aria-label="Photo of a woman on a forest bridge seen from behind"></div>
  <svg class="fill" viewBox="0 0 396 223" preserveAspectRatio="none"><path d="M0 175C150 150 280 200 396 138V223H0Z" fill="var(--teal)"/></svg>
  <div class="a white" style="left:16px;top:184px;font-size:13px;font-weight:700;line-height:1">SECTION DIVIDER</div>
  <div class="a white" style="left:16px;top:198px;font-size:6px">SECTION SUBTITLE</div>
  <div class="brand" style="left:338px;top:202px;font-size:6px">dorneck-saalig</div>
</section>

<!-- 10 about me -->
<section class="slide">
  <div class="a" style="left:0;top:0;width:90px;height:100%;background:#d9dfe0"></div>
  <div class="card" style="left:42px;top:38px;width:86px;height:144px;border-radius:4px;padding:5px"><div class="ph-portrait" style="width:100%;height:100%;border-radius:3px" role="img" aria-label="Portrait photo of the coach"></div></div>
  <div class="a h" style="left:150px;top:46px;font-size:14px">Über Mich</div>
  <div class="a t" style="left:158px;top:72px;width:200px;font-size:4.8px"><span style="color:var(--teal)">➤</span> If I use <b style="font-size:7px">bullet points</b> out of the standard bullet point tools… I only have the regular bullets → can you include the nicer ones (from the slides below)? Or in my corporate colors?</div>
  <div class="a t" style="left:158px;top:104px;font-size:4.8px"><span style="color:var(--teal)">➤</span> Test text test</div>
  <div class="a t" style="left:158px;top:118px;font-size:4.8px"><span style="color:var(--teal)">➤</span> Test text test</div>
  <div class="page">PAGE | 12</div>
</section>

<!-- 11 program context -->
<section class="slide">
  <div class="a" style="left:0;top:0;width:128px;height:100%;background:var(--teal)"></div>
  <div class="a white" style="left:14px;top:36px;font-size:13px;font-weight:700;line-height:1.2">Program<br>context and<br>deliverables<br>slide</div>
  <p class="a white" style="left:14px;top:120px;width:104px;font-size:4.4px;line-height:1.45;text-align:justify">Lorem ipsum dolor sit amet, consectetur adipiscing elit, sed do eiusmod tempor incididunt ut labore et dolore magna aliqua. Lorem ipsum dolor sit amet, consectetur adipiscing elit, sed do eiusmod tempor incididunt ut labore et dolore magna aliqua. Ut enim ad minim veniam, quis nostrud exercitation ullamco laboris nisi ut aliquip.</p>
  <div class="a ph-waterfall" style="left:128px;top:0;width:135px;height:100%" role="img" aria-label="Photo of a person in front of a forest waterfall"></div>
  <div class="a" style="left:272px;top:44px;width:112px">
    <div style="color:var(--teal);font-size:4.8px;font-weight:500">Strategy for online Learning</div><p class="t">Lorem ipsum dolor sit amet, consectetur adipiscing elit, sed do eiusmod tempor incididunt ut labore et dolore magna aliqua. Lorem ipsum dolor sit amet, sed do eiusmod</p>
    <div style="color:var(--teal);font-size:4.8px;font-weight:500;margin-top:12px">Strategy for online Learning</div><p class="t">Lorem ipsum dolor sit amet, consectetur adipiscing elit, sed do eiusmod tempor incididunt ut labore et dolore magna aliqua. Lorem ipsum dolor sit amet, sed do eiusmod</p>
    <div style="color:var(--teal);font-size:4.8px;font-weight:500;margin-top:12px">Strategy for online Learning</div><p class="t">Lorem ipsum dolor sit amet, consectetur adipiscing elit, sed do eiusmod tempor incididunt ut labore et dolore magna aliqua. Lorem ipsum dolor sit amet, sed do eiusmod</p>
  </div>
  <div class="page">PAGE | 13</div>
</section>

<!-- 12 tower pink bullets -->
<section class="slide">
  <div class="a ph-tower" style="left:0;top:0;width:198px;height:206px" role="img" aria-label="Photo of a glass tower seen from below"></div>
  <p class="a white" style="left:34px;top:64px;width:130px;text-align:center;font-size:7.5px;line-height:1.35">Lorem ipsum dolor sit amet, consectetur adipiscing elit, sed do eiusmod tempor incididunt ut labore et dolore magna aliqua. Lorem ipsum dolor sit amet, consectetur adipiscing elit, sed do eiusmod tempor incididunt ut labore et dolore magna aliqua.</p>
  <p class="a" style="left:222px;top:48px;width:160px;font-size:4.8px;line-height:1.35;color:var(--teal)">Lorem ipsum dolor sit amet, consectetur adipiscing elit, sed do eiusmod tempor incididunt ut labore et dolore magna aliqua. Lorem ipsum dolor sit amet, consectetur adipiscing elit, sed do eiusmod tempor incididunt ut labore et dolore magna aliqua.</p>
  <div class="bullet-row t" style="left:227px;top:100px;width:155px"><i></i><span>Lorem ipsum dolor sit amet, consectetur adipiscing elit, sed do eiusmod tempor incididunt ut labore et dolore magna aliqua.</span></div>
  <div class="bullet-row t" style="left:227px;top:122px;width:155px"><i></i><span>Lorem ipsum dolor sit amet, consectetur adipiscing elit, sed do eiusmod tempor incididunt ut labore et dolore magna aliqua.</span></div>
  <div class="bullet-row t" style="left:227px;top:144px;width:155px"><i></i><span>Lorem ipsum dolor sit amet, consectetur adipiscing elit, sed do eiusmod tempor incididunt ut labore et dolore magna aliqua.</span></div>
  <div class="bullet-row t" style="left:227px;top:166px;width:155px"><i></i><span>Lorem ipsum dolor sit amet, consectetur adipiscing elit, sed do eiusmod tempor incididunt ut labore et dolore magna aliqua.</span></div>
  <div class="brand sm">dorneck-saalig</div><div class="page">PAGE | 14</div>
</section>

<!-- 13 tower teal bullets -->
<section class="slide">
  <div class="a ph-tower" style="left:0;top:0;width:198px;height:206px" role="img" aria-label="Photo of a glass tower seen from below"></div>
  <p class="a white" style="left:34px;top:64px;width:130px;text-align:center;font-size:7.5px;line-height:1.35">Lorem ipsum dolor sit amet, consectetur adipiscing elit, sed do eiusmod tempor incididunt ut labore et dolore magna aliqua. Lorem ipsum dolor sit amet, consectetur adipiscing elit, sed do eiusmod tempor incididunt ut labore et dolore magna aliqua.</p>
  <p class="a" style="left:222px;top:48px;width:150px;font-size:4.8px;line-height:1.35;color:var(--teal);font-weight:500">Lorem ipsum dolor sit amet, consectetur adipiscing elit, sed do eiusmod tempor incididunt ut labore et dolore magna aliqua. Lorem ipsum dolor sit amet, consectetur adipiscing elit, sed do eiusmod tempor incididunt ut labore et dolore magna aliqua.</p>
  <div class="bullet-row t" style="left:227px;top:100px;width:145px"><i style="border-color:var(--teal)"></i><span>Lorem ipsum dolor sit amet, consectetur adipiscing elit, sed do eiusmod tempor incididunt ut labore et dolore magna aliqua.</span></div>
  <div class="bullet-row t" style="left:227px;top:122px;width:145px"><i style="border-color:var(--teal)"></i><span>Lorem ipsum dolor sit amet, consectetur adipiscing elit, sed do eiusmod tempor incididunt ut labore et dolore magna aliqua.</span></div>
  <div class="bullet-row t" style="left:227px;top:144px;width:145px"><i style="border-color:var(--teal)"></i><span>Lorem ipsum dolor sit amet, consectetur adipiscing elit, sed do eiusmod tempor incididunt ut labore et dolore magna aliqua.</span></div>
  <div class="bullet-row t" style="left:227px;top:166px;width:145px"><i style="border-color:var(--teal)"></i><span>Lorem ipsum dolor sit amet, consectetur adipiscing elit, sed do eiusmod tempor incididunt ut labore et dolore magna aliqua.</span></div>
  <div class="brand sm">dorneck-saalig</div><div class="page">PAGE | 15</div>
</section>

<!-- 14 test headline cards -->
<section class="slide mist">
  <div class="accent-line" style="left:26px;top:16px;height:18px"></div>
  <div class="a h" style="left:28px;top:15px;font-size:13px;color:var(--ink)">Test Headline</div>
  <div class="a t" style="left:28px;top:32px">Test Sub Headline</div>
  <article class="card" style="left:36px;top:52px;width:92px;height:132px;border-bottom:2px solid var(--pink);padding:10px 8px">
    <div class="h" style="font-size:7px;line-height:1.15">Add Awesome<br>Title Here</div><p class="t" style="margin:6px 0 10px">Lorem ipsum dolor sit amet, consectetur adipiscing elit, sed do eiusmod tempor incididunt ut labore et dolore magna aliqua.</p>
    <p class="t">○ Lorem ipsum dolor sit amet, consectetur adipiscing elit, sed</p><p class="t" style="margin-top:4px">○ Lorem ipsum dolor sit amet, consectetur adipiscing elit, sed</p><p class="t" style="margin-top:4px">○ Lorem ipsum dolor sit amet, consectetur adipiscing elit, sed</p>
  </article>
  <article class="card" style="left:148px;top:52px;width:92px;height:132px;border-bottom:2px solid var(--pink);padding:10px 8px">
    <div class="h" style="font-size:7px;line-height:1.15">Add Awesome<br>Title Here</div><p class="t" style="margin:6px 0 10px">Lorem ipsum dolor sit amet, consectetur adipiscing elit, sed do eiusmod tempor incididunt ut labore et dolore magna aliqua.</p>
    <p class="t">○ Lorem ipsum dolor sit amet, consectetur adipiscing elit, sed</p><p class="t" style="margin-top:4px">○ Lorem ipsum dolor sit amet, consectetur adipiscing elit, sed</p><p class="t" style="margin-top:4px">○ Lorem ipsum dolor sit amet, consectetur adipiscing elit, sed</p>
  </article>
  <article class="card" style="left:260px;top:52px;width:92px;height:132px;border-bottom:2px solid var(--pink);padding:10px 8px">
    <div class="h" style="font-size:7px;line-height:1.15">Add Awesome<br>Title Here</div><p class="t" style="margin:6px 0 10px">Lorem ipsum dolor sit amet, consectetur adipiscing elit, sed do eiusmod tempor incididunt ut labore et dolore magna aliqua.</p>
    <p class="t">○ Lorem ipsum dolor sit amet, consectetur adipiscing elit, sed</p><p class="t" style="margin-top:4px">○ Lorem ipsum dolor sit amet, consectetur adipiscing elit, sed</p><p class="t" style="margin-top:4px">○ Lorem ipsum dolor sit amet, consectetur adipiscing elit, sed</p>
  </article>
  <div class="brand sm">dorneck-saalig</div><div class="page">PAGE | 16</div>
</section>

<!-- 15 project icons -->
<section class="slide mist">
  <div class="accent-line"></div>
  <div class="dot" style="left:36px;top:72px;width:24px;height:24px;background:var(--silver);box-shadow:0 0 0 3px #e4e8e9"></div>
  <div class="a" style="left:68px;top:67px;width:108px"><div class="h" style="font-size:5px">Project name</div><p class="t">Lorem ipsum dolor sit amet, nec an dictas equidem appellantur, ut has commune accommodare. Mea illum, ludus solet idpro.</p></div>
  <div class="dot" style="left:36px;top:114px;width:24px;height:24px;background:var(--silver);box-shadow:0 0 0 3px #e4e8e9"></div>
  <div class="a" style="left:68px;top:109px;width:108px"><div class="h" style="font-size:5px">Project name</div><p class="t">Lorem ipsum dolor sit amet, nec an dictas equidem appellantur, ut has commune accommodare. Mea illum, ludus solet idpro.</p></div>
  <div class="dot" style="left:36px;top:156px;width:24px;height:24px;background:var(--silver);box-shadow:0 0 0 3px #e4e8e9"></div>
  <div class="a" style="left:68px;top:151px;width:108px"><div class="h" style="font-size:5px">Project name</div><p class="t">Lorem ipsum dolor sit amet, nec an dictas equidem appellantur, ut has commune accommodare. Mea illum, ludus solet idpro.</p></div>
  <div class="dot" style="left:206px;top:72px;width:24px;height:24px;background:var(--silver);box-shadow:0 0 0 3px #e4e8e9"></div>
  <div class="a" style="left:238px;top:67px;width:108px"><div class="h" style="font-size:5px">Project name</div><p class="t">Lorem ipsum dolor sit amet, nec an dictas equidem appellantur, ut has commune accommodare. Mea illum, ludus solet idpro.</p></div>
  <div class="dot" style="left:206px;top:114px;width:24px;height:24px;background:var(--silver);box-shadow:0 0 0 3px #e4e8e9"></div>
  <div class="a" style="left:238px;top:109px;width:108px"><div class="h" style="font-size:5px">Project name</div><p class="t">Lorem ipsum dolor sit amet, nec an dictas equidem appellantur, ut has commune accommodare. Mea illum, ludus solet idpro.</p></div>
  <div class="dot" style="left:206px;top:156px;width:24px;height:24px;background:var(--silver);box-shadow:0 0 0 3px #e4e8e9"></div>
  <div class="a" style="left:238px;top:151px;width:108px"><div class="h" style="font-size:5px">Project name</div><p class="t">Lorem ipsum dolor sit amet, nec an dictas equidem appellantur, ut has commune accommodare. Mea illum, ludus solet idpro.</p></div>
  <div class="brand sm">dorneck-saalig</div><div class="page">PAGE | 17</div>
</section>

<!-- 16 numbered list -->
<section class="slide mist">
  <div class="accent-line"></div>
  <div class="dot white" style="left:26px;top:70px;width:14px;height:14px;background:var(--teal);font-size:4.5px">01</div><div class="a" style="left:46px;top:71px"><div class="h" style="font-size:4.8px">Your Text Here</div><p class="t">Lorem ipsum dolor sit amet.</p></div>
  <div class="dot white" style="left:140px;top:70px;width:14px;height:14px;background:var(--teal);font-size:4.5px">02</div><div class="a" style="left:160px;top:71px"><div class="h" style="font-size:4.8px">Your Text Here</div><p class="t">Lorem ipsum dolor sit amet.</p></div>
  <div class="dot white" style="left:258px;top:70px;width:14px;height:14px;background:var(--teal);font-size:4.5px">03</div><div class="a" style="left:278px;top:71px"><div class="h" style="font-size:4.8px">Your Text Here</div><p class="t">Lorem ipsum dolor sit amet.</p></div>
  <div class="dot white" style="left:26px;top:99px;width:14px;height:14px;background:var(--teal);font-size:4.5px">04</div><div class="a" style="left:46px;top:100px"><div class="h" style="font-size:4.8px">Your Text Here</div><p class="t">Lorem ipsum dolor sit amet.</p></div>
  <div class="dot white" style="left:140px;top:99px;width:14px;height:14px;background:var(--teal);font-size:4.5px">05</div><div class="a" style="left:160px;top:100px"><div class="h" style="font-size:4.8px">Your Text Here</div><p class="t">Lorem ipsum dolor sit amet.</p></div>
  <div class="dot white" style="left:258px;top:99px;width:14px;height:14px;background:var(--teal);font-size:4.5px">06</div><div class="a" style="left:278px;top:100px"><div class="h" style="font-size:4.8px">Your Text Here</div><p class="t">Lorem ipsum dolor sit amet.</p></div>
  <div class="dot white" style="left:26px;top:128px;width:14px;height:14px;background:var(--teal);font-size:4.5px">07</div><div class="a" style="left:46px;top:129px"><div class="h" style="font-size:4.8px">Your Text Here</div><p class="t">Lorem ipsum dolor sit amet.</p></div>
  <div class="dot white" style="left:140px;top:128px;width:14px;height:14px;background:var(--teal);font-size:4.5px">08</div><div class="a" style="left:160px;top:129px"><div class="h" style="font-size:4.8px">Your Text Here</div><p class="t">Lorem ipsum dolor sit amet.</p></div>
  <div class="dot white" style="left:258px;top:128px;width:14px;height:14px;background:var(--teal);font-size:4.5px">09</div><div class="a" style="left:278px;top:129px"><div class="h" style="font-size:4.8px">Your Text Here</div><p class="t">Lorem ipsum dolor sit amet.</p></div>
  <div class="dot white" style="left:26px;top:157px;width:14px;height:14px;background:var(--teal);font-size:4.5px">10</div><div class="a" style="left:46px;top:158px"><div class="h" style="font-size:4.8px">Your Text Here</div><p class="t">Lorem ipsum dolor sit amet.</p></div>
  <div class="dot white" style="left:140px;top:157px;width:14px;height:14px;background:var(--teal);font-size:4.5px">11</div><div class="a" style="left:160px;top:158px"><div class="h" style="font-size:4.8px">Your Text Here</div><p class="t">Lorem ipsum dolor sit amet.</p></div>
  <div class="dot white" style="left:258px;top:157px;width:14px;height:14px;background:var(--teal);font-size:4.5px">12</div><div class="a" style="left:278px;top:158px"><div class="h" style="font-size:4.8px">Your Text Here</div><p class="t">Lorem ipsum dolor sit amet.</p></div>
  <div class="brand sm">dorneck-saalig</div><div class="page">PAGE | 18</div>
</section>

<!-- 17 awesome three photos -->
<section class="slide">
  <div class="a" style="left:0;top:0;width:100%;height:118px;background:var(--silver)"></div>
  <div class="a white" style="left:22px;top:34px;font-size:13px;font-weight:500;line-height:1.2">Your awesome<br>text here</div>
  <div class="a white" style="left:22px;top:68px;font-size:4px;letter-spacing:2px">SUB TITLE GOES HERE</div>
  <p class="a white" style="left:190px;top:30px;width:190px;font-size:4.4px;line-height:1.4">Lorem ipsum dolor sit amet, consectetur adipiscing elit, sed do eiusmod tempor incididunt ut labore et dolore magna aliqua. Lorem ipsum dolor sit amet, consectetur adipiscing elit, sed do eiusmod tempor incididunt ut labore et dolore magna aliqua. Ut enim ad minim veniam, quis nostrud exercitation ullamco laboris nisi.</p>
  <div class="a ph-compass" style="left:22px;top:90px;width:98px;height:64px;border-radius:3px" role="img" aria-label="Photo of a compass held against a landscape"></div>
  <div class="a ph-laptop" style="left:150px;top:90px;width:98px;height:64px;border-radius:3px" role="img" aria-label="Photo of hands typing on a laptop"></div>
  <div class="a ph-meeting" style="left:280px;top:90px;width:98px;height:64px;border-radius:3px" role="img" aria-label="Photo of a bright meeting room"></div>
  <div class="a" style="left:22px;top:162px;width:98px"><div class="h" style="font-size:5px">Your Text Here</div><p class="t">Lorem ipsum dolor sit amet, consectetur adipiscing elit, sed do eiusmod tempor incididunt ut labore et dolore magna aliqua.</p></div>
  <div class="a" style="left:150px;top:162px;width:98px"><div class="h" style="font-size:5px">Your Text Here</div><p class="t">Lorem ipsum dolor sit amet, consectetur adipiscing elit, sed do eiusmod tempor incididunt ut labore et dolore magna aliqua.</p></div>
  <div class="a" style="left:280px;top:162px;width:98px"><div class="h" style="font-size:5px">Your Text Here</div><p class="t">Lorem ipsum dolor sit amet, consectetur adipiscing elit, sed do eiusmod tempor incididunt ut labore et dolore magna aliqua.</p></div>
  <div class="brand sm">dorneck-saalig</div><div class="page">PAGE | 19</div>
</section>

<!-- 18 city -->
<section class="slide">
  <div class="a ph-street" style="left:60px;top:0;width:336px;height:204px;border-bottom-left-radius:60px" role="img" aria-label="Photo of a busy city street at sunset"></div>
  <div class="a" style="left:0;top:110px;width:196px;height:92px;background:var(--teal)"></div>
  <div class="a white" style="left:22px;top:118px;font-size:13px;font-weight:500">Your Text Here</div>
  <p class="a white" style="left:22px;top:138px;width:160px;font-size:4.6px;line-height:1.4">Lorem Ipsum the printing and typesetting industry. Lorem Ipsum has been the industry's standard dummy text ever since the 1500s, when an unknown printer took a galley of type and scrambled it to make a type specimen book. It has survived not only five centuries.</p>
  <div class="brand sm">dorneck-saalig</div><div class="page">PAGE | 20</div>
</section>

<!-- 19 add awesome 50% -->
<section class="slide">
  <div class="a h" style="left:28px;top:36px;font-size:12px;line-height:1.1">Add your awesome<br>text here</div>
  <div class="a" style="left:22px;top:72px;width:325px;height:118px;background:#f0f2f2;border-radius:4px"></div>
  <p class="a t" style="left:34px;top:86px;width:150px;text-align:justify">There are many variations of passages of Lorem Ipsum available, but the majority have suffered alteration in some form, by injected humour, or randomised words which don't look even slightly believable. If you are going to use a passage of Lorem Ipsum, you need to be sure there isn't anything embarrassing hidden in the middle of text. All the Lorem Ipsum generators on the Internet tend to repeat predefined chunks as necessary, making this the first true generator on the Internet. There are many variations of passages of Lorem Ipsum available, but the majority have suffered alteration in some form, by injected humour, or randomised words which don't look even slightly believable.</p>
  <div class="a ph-lightbox" style="left:200px;top:22px;width:180px;height:112px;border-radius:6px" role="img" aria-label="Photo of a lightbox sign on a chair"></div>
  <div class="stat-circle" style="left:212px;top:118px;background:var(--teal)"><b>50%</b><span>Lorem ipsum dolor sit amet, consectetur adipiscing elit</span></div>
  <div class="brand sm">dorneck-saalig</div><div class="page">PAGE | 22</div>
</section>

<!-- 20 add awesome boxes -->
<section class="slide">
  <div class="a h" style="left:24px;top:26px;font-size:12px;line-height:1.1">Add your Awesome<br>Text Here</div>
  <p class="a t" style="left:24px;top:56px;width:178px;color:var(--ink);text-align:justify">Lorem Ipsum the printing and typesetting industry. Lorem Ipsum has been the industry's standard dummy text ever since the 1500s, when an unknown printer took a galley of type and scrambled it to make a type specimen book. It has survived not only five centuries.</p>
  <div class="a ph-sticky" style="left:234px;top:14px;width:148px;height:192px;border-radius:6px" role="img" aria-label="Photo of a hand placing sticky notes on a wall"></div>
  <div class="a" style="left:24px;top:110px;width:78px;height:80px;background:var(--teal);border-radius:3px;text-align:center;padding-top:30px"><div class="white" style="font-size:4.8px;font-weight:500">Project name</div><p class="white" style="font-size:3.8px;line-height:1.4;padding:2px 6px">Lorem ipsum dolor sit amet, nec an dictas equidem appellantur, ut has commune accommodare. Mea illum, ludus solet idpro.</p></div>
  <div class="card" style="left:108px;top:110px;width:78px;height:80px;border-radius:3px;text-align:center;padding-top:30px"><div class="h" style="font-size:4.8px">Project name</div><p class="t" style="font-size:3.8px;padding:2px 6px">Lorem ipsum dolor sit amet, nec an dictas equidem appellantur, ut has commune accommodare. Mea illum, ludus solet idpro.</p></div>
  <div class="card" style="left:192px;top:110px;width:78px;height:80px;border-radius:3px;text-align:center;padding-top:30px"><div class="h" style="font-size:4.8px">Project name</div><p class="t" style="font-size:3.8px;padding:2px 6px">Lorem ipsum dolor sit amet, nec an dictas equidem appellantur, ut has commune accommodare. Mea illum, ludus solet idpro.</p></div>
  <div class="brand sm">dorneck-saalig</div><div class="page">PAGE | 23</div>
</section>

<!-- 21 three panels -->
<section class="slide">
  <div class="a h" style="left:18px;top:48px;font-size:12px;line-height:1.2">Lorem ipsum dolor sit<br>amet elit et dolor</div>
  <p class="a t" style="left:18px;top:82px;width:146px">Lorem ipsum dolor sit amet, consectetur adipiscing elit, sed do eiusmod tempor incididunt ut labore et dolore magna aliqua. Lorem ipsum dolor sit amet, consectetur adipiscing elit, sed do eiusmod.</p>
  <div class="a ph-office" style="left:172px;top:18px;width:210px;height:118px" role="img" aria-label="Photo of a modern office with large windows"></div>
  <div class="a" style="left:0;top:138px;width:132px;height:85px;background:var(--teal)"></div>
  <div class="a" style="left:132px;top:138px;width:132px;height:85px;background:var(--pink)"></div>
  <div class="a" style="left:264px;top:138px;width:132px;height:85px;background:var(--silver)"></div>
  <div class="dot" style="left:22px;top:124px;width:26px;height:26px;background:var(--teal);border:2px solid #fff"></div>
  <div class="dot" style="left:152px;top:124px;width:26px;height:26px;background:var(--pink);border:2px solid #fff"></div>
  <div class="dot" style="left:284px;top:124px;width:26px;height:26px;background:var(--silver);border:2px solid #fff"></div>
  <div class="a white" style="left:14px;top:163px;width:110px"><div style="font-size:5.5px;font-weight:500">Lorem ipsum dolor</div><p style="font-size:4.2px;line-height:1.4">Lorem ipsum dolor sit amet, consectetur adipiscing elit, sed do eiusmod tempor incididunt ut labore et dolore magna aliqua.</p></div>
  <div class="a" style="left:146px;top:163px;width:110px;color:var(--ink)"><div style="font-size:5.5px;font-weight:500">Lorem ipsum dolor</div><p style="font-size:4.2px;line-height:1.4">Lorem ipsum dolor sit amet, consectetur adipiscing elit, sed do eiusmod tempor incididunt ut labore et dolore magna aliqua.</p></div>
  <div class="a white" style="left:278px;top:163px;width:110px"><div style="font-size:5.5px;font-weight:500">Lorem ipsum dolor</div><p style="font-size:4.2px;line-height:1.4">Lorem ipsum dolor sit amet, consectetur adipiscing elit, sed do eiusmod tempor incididunt ut labore et dolore magna aliqua.</p></div>
</section>

<!-- 22 cycle -->
<section class="slide">
  <div class="accent-line"></div>
  <svg class="a" style="left:136px;top:58px" width="132" height="132" viewBox="0 0 132 132">
    <circle cx="66" cy="66" r="52" fill="none" stroke="var(--teal)" stroke-width="20" stroke-dasharray="48 6.4"/>
    <circle cx="66" cy="66" r="40" fill="#fff"/>
  </svg>
  <div class="a" style="left:170px;top:118px;width:64px;text-align:center;font-size:8px;font-weight:500;color:var(--ink)">dorneck-saalig</div>
  <div class="a" style="left:32px;top:60px;width:110px;text-align:right"><div class="h" style="font-size:5px">Lorem ipsum dolor</div><p class="t">Lorem ipsum dolor sit amet, consectetur adipiscing elit, sed do eiusmod tempor</p></div>
  <div class="a" style="left:12px;top:114px;width:110px;text-align:right"><div class="h" style="font-size:5px">Lorem ipsum dolor</div><p class="t">Lorem ipsum dolor sit amet, consectetur adipiscing elit, sed do eiusmod tempor</p></div>
  <div class="a" style="left:32px;top:170px;width:110px;text-align:right"><div class="h" style="font-size:5px">Lorem ipsum dolor</div><p class="t">Lorem ipsum dolor sit amet, consectetur adipiscing elit, sed do eiusmod tempor</p></div>
  <div class="a" style="left:256px;top:56px;width:115px"><div class="h" style="font-size:5px">Lorem ipsum dolor</div><p class="t">Lorem ipsum dolor sit amet, consectetur adipiscing elit, sed do eiusmod tempor</p></div>
  <div class="a" style="left:280px;top:114px;width:106px"><div class="h" style="font-size:5px">Lorem ipsum dolor</div><p class="t">Lorem ipsum dolor sit amet, consectetur adipiscing elit, sed do eiusmod tempor</p></div>
  <div class="a" style="left:258px;top:170px;width:115px"><div class="h" style="font-size:5px">Lorem ipsum dolor</div><p class="t">Lorem ipsum dolor sit amet, consectetur adipiscing elit, sed do eiusmod tempor</p></div>
  <div class="brand sm">dorneck-saalig</div><div class="page">PAGE | 25</div>
</section>

<!-- 23 timeline -->
<section class="slide">
  <div class="accent-line"></div>
  <div class="a" style="left:56px;top:128px;width:296px;height:1px;background:var(--silver)"></div>
  <div class="dot" style="left:42px;top:114px;width:28px;height:28px;background:var(--teal);border:3px solid #e0f1f0"></div>
  <div class="dot" style="left:112px;top:114px;width:28px;height:28px;background:var(--pink);border:3px solid #fbefe8"></div>
  <div class="dot" style="left:184px;top:114px;width:28px;height:28px;background:var(--teal);border:3px solid #e0f1f0"></div>
  <div class="dot" style="left:254px;top:114px;width:28px;height:28px;background:var(--pink);border:3px solid #fbefe8"></div>
  <div class="dot" style="left:322px;top:114px;width:28px;height:28px;background:var(--teal);border:3px solid #e0f1f0"></div>
  <div class="a" style="left:18px;top:68px;width:76px;text-align:center"><div class="h" style="font-size:4.8px">Content Title here</div><p class="t">Lorem ipsum dolor sit amet, nec an dictas equidem appellantur, ut has commune</p></div>
  <div class="a" style="left:160px;top:68px;width:76px;text-align:center"><div class="h" style="font-size:4.8px">Content Title here</div><p class="t">Lorem ipsum dolor sit amet, nec an dictas equidem appellantur, ut has commune</p></div>
  <div class="a" style="left:298px;top:68px;width:76px;text-align:center"><div class="h" style="font-size:4.8px">Content Title here</div><p class="t">Lorem ipsum dolor sit amet, nec an dictas equidem appellantur, ut has commune</p></div>
  <div class="a" style="left:88px;top:158px;width:76px;text-align:center"><div class="h" style="font-size:4.8px">Content Title here</div><p class="t">Promotion an ourselves up otherwise my. High what each snug rich to inhabiting.</p></div>
  <div class="a" style="left:230px;top:158px;width:76px;text-align:center"><div class="h" style="font-size:4.8px">Content Title here</div><p class="t">Promotion an ourselves up otherwise my. High what each snug rich to inhabiting.</p></div>
  <div class="brand sm">dorneck-saalig</div><div class="page">PAGE | 26</div>
</section>

<!-- 24 table -->
<section class="slide">
  <div class="accent-line"></div>
  <div class="a" style="left:36px;top:64px;width:325px;display:grid;grid-template-columns:repeat(4,1fr);gap:1px;background:#fff">
    <div style="background:var(--teal-dark);color:#fff;font-size:4.8px;padding:5px 3px">ADD YOUR TITLE</div><div style="background:var(--teal-dark);color:#fff;font-size:4.8px;padding:5px 3px">ADD YOUR TITLE</div><div style="background:var(--teal-dark);color:#fff;font-size:4.8px;padding:5px 3px">ADD YOUR TITLE</div><div style="background:var(--teal-dark);color:#fff;font-size:4.8px;padding:5px 3px">ADD YOUR TITLE</div>
    <div style="background:var(--silver);color:#fff;padding:5px 6px;height:42px"><b style="font-size:4.6px;font-weight:500">Project name</b><p style="font-size:3.6px;line-height:1.35;padding:2px 4px">Lorem Ipsum is simply dummy unknown printer took a galley of type and scrambled it to make.</p></div>
    <div style="background:var(--teal);color:#fff;padding:5px 6px"><b style="font-size:4.6px;font-weight:500">Project name</b><p style="font-size:3.6px;line-height:1.35;padding:2px 4px">Lorem Ipsum is simply dummy unknown printer took a galley of type and scrambled it to make.</p></div>
    <div style="background:var(--teal);color:#fff;padding:5px 6px"><b style="font-size:4.6px;font-weight:500">Project name</b><p style="font-size:3.6px;line-height:1.35;padding:2px 4px">Lorem Ipsum is simply dummy unknown printer took a galley of type and scrambled it to make.</p></div>
    <div style="background:var(--teal);color:#fff;padding:5px 6px"><b style="font-size:4.6px;font-weight:500">Project name</b><p style="font-size:3.6px;line-height:1.35;padding:2px 4px">Lorem Ipsum is simply dummy unknown printer took a galley of type and scrambled it to make.</p></div>
    <div style="background:var(--silver);color:#fff;padding:5px 6px;height:42px"><b style="font-size:4.6px;font-weight:500">Project name</b><p style="font-size:3.6px;line-height:1.35;padding:2px 4px">Lorem Ipsum is simply dummy unknown printer took a galley of type and scrambled it to make.</p></div>
    <div style="background:var(--teal);color:#fff;padding:5px 6px"><b style="font-size:4.6px;font-weight:500">Project name</b><p style="font-size:3.6px;line-height:1.35;padding:2px 4px">Lorem Ipsum is simply dummy unknown printer took a galley of type and scrambled it to make.</p></div>
    <div style="background:var(--teal);color:#fff;padding:5px 6px"><b style="font-size:4.6px;font-weight:500">Project name</b><p style="font-size:3.6px;line-height:1.35;padding:2px 4px">Lorem Ipsum is simply dummy unknown printer took a galley of type and scrambled it to make.</p></div>
    <div style="background:var(--teal);color:#fff;padding:5px 6px"><b style="font-size:4.6px;font-weight:500">Project name</b><p style="font-size:3.6px;line-height:1.35;padding:2px 4px">Lorem Ipsum is simply dummy unknown printer took a galley of type and scrambled it to make.</p></div>
  </div>
  <div class="brand sm">dorneck-saalig</div><div class="page">PAGE | 27</div>
</section>

<!-- 25 money circles -->
<section class="slide">
  <div class="accent-line"></div>
  <div class="stat-circle" style="left:38px;top:56px;background:var(--teal)"><b>$1M</b><span>Lorem ipsum dolor sit amet, nec an dictas equidem appellantur, ut has commune</span></div>
  <div class="stat-circle" style="left:160px;top:56px;background:var(--pink)"><b>$10M</b><span>Lorem ipsum dolor sit amet, nec an dictas equidem appellantur, ut has commune</span></div>
  <div class="stat-circle" style="left:284px;top:56px;background:var(--silver)"><b>$15M</b><span>Lorem ipsum dolor sit amet, nec an dictas equidem appellantur, ut has commune</span></div>
  <div class="a" style="left:26px;top:150px;width:100px;text-align:center"><div class="h" style="font-size:5px">Lorem ipsum dolor</div><p class="t">Lorem ipsum dolor sit amet, consectetur adipiscing elit, sed do eiusmod tempor</p></div>
  <div class="a" style="left:148px;top:150px;width:100px;text-align:center"><div class="h" style="font-size:5px">Lorem ipsum dolor</div><p class="t">Lorem ipsum dolor sit amet, consectetur adipiscing elit, sed do eiusmod tempor</p></div>
  <div class="a" style="left:272px;top:150px;width:100px;text-align:center"><div class="h" style="font-size:5px">Lorem ipsum dolor</div><p class="t">Lorem ipsum dolor sit amet, consectetur adipiscing elit, sed do eiusmod tempor</p></div>
  <div class="brand sm">dorneck-saalig</div><div class="page">PAGE | 28</div>
</section>

<!-- 26 percentages -->
<section class="slide">
  <div class="a h" style="left:0;right:0;top:40px;text-align:center;font-size:17px">Your awesome text here</div>
  <p class="a t" style="left:74px;top:64px;width:248px;text-align:center;color:var(--ink)">Lorem Ipsum the printing and typesetting industry. Lorem Ipsum has been the industry's standard dummy text ever since the 1500s, when an unknown printer took a galley of type and scrambled it to make a type specimen book. It has survived not only five centuries.</p>
  <svg class="a" style="left:80px;top:100px" width="240" height="60" viewBox="0 0 240 60">
    <g fill="none" stroke-width="3">
      <circle cx="30" cy="30" r="24" stroke="#eceeee"/><circle cx="30" cy="30" r="24" stroke="var(--teal)" stroke-dasharray="75.4 150.8" transform="rotate(-90 30 30)"/>
      <circle cx="120" cy="30" r="24" stroke="#eceeee"/><circle cx="120" cy="30" r="24" stroke="var(--teal)" stroke-dasharray="113.1 150.8" transform="rotate(-90 120 30)"/>
      <circle cx="210" cy="30" r="24" stroke="#eceeee"/><circle cx="210" cy="30" r="24" stroke="var(--silver)" stroke-dasharray="60.3 150.8" transform="rotate(-90 210 30)"/>
    </g>
    <g font-family="Roboto, sans-serif" font-size="14" font-weight="500" fill="#666" text-anchor="middle"><text x="30" y="35">50%</text><text x="120" y="35">75%</text><text x="210" y="35">40%</text></g>
  </svg>
  <p class="a t" style="left:78px;top:170px;width:64px;text-align:center">Lorem ipsum dolor amet amet consectetur dolor</p>
  <p class="a t" style="left:168px;top:170px;width:64px;text-align:center">Lorem ipsum dolor amet amet consectetur dolor</p>
  <p class="a t" style="left:258px;top:170px;width:64px;text-align:center">Lorem ipsum dolor amet amet consectetur dolor</p>
  <div class="brand sm">dorneck-saalig</div><div class="page">PAGE | 29</div>
</section>

<!-- 27 company statistics -->
<section class="slide">
  <svg class="a" style="left:8px;top:34px" width="200" height="150" viewBox="0 0 200 150">
    <g stroke="#e6e6e6" stroke-width=".5"><line x1="20" y1="8" x2="200" y2="8"/><line x1="20" y1="21" x2="200" y2="21"/><line x1="20" y1="34" x2="200" y2="34"/><line x1="20" y1="47" x2="200" y2="47"/><line x1="20" y1="60" x2="200" y2="60"/><line x1="20" y1="73" x2="200" y2="73"/><line x1="20" y1="86" x2="200" y2="86"/><line x1="20" y1="99" x2="200" y2="99"/><line x1="20" y1="112" x2="200" y2="112"/><line x1="20" y1="125" x2="200" y2="125"/><line x1="20" y1="138" x2="200" y2="138"/></g>
    <g font-family="Roboto, sans-serif" font-size="4" fill="#999" text-anchor="end"><text x="14" y="10">5</text><text x="14" y="23">4.5</text><text x="14" y="36">4</text><text x="14" y="49">3.5</text><text x="14" y="62">3</text><text x="14" y="75">2.5</text><text x="14" y="88">2</text><text x="14" y="101">1.5</text><text x="14" y="114">1</text><text x="14" y="127">0.5</text><text x="14" y="140">0</text></g>
    <rect x="28" y="34" width="6" height="104" fill="var(--teal)"/><rect x="35" y="73" width="6" height="65" fill="var(--silver)"/><rect x="42" y="86" width="6" height="52" fill="var(--pink)"/>
    <rect x="68" y="86" width="6" height="52" fill="var(--teal)"/><rect x="75" y="34" width="6" height="104" fill="var(--silver)"/><rect x="82" y="86" width="6" height="52" fill="var(--pink)"/>
    <rect x="108" y="47" width="6" height="91" fill="var(--teal)"/><rect x="115" y="112" width="6" height="26" fill="var(--silver)"/><rect x="122" y="112" width="6" height="26" fill="var(--pink)"/>
    <rect x="148" y="112" width="6" height="26" fill="var(--teal)"/><rect x="155" y="60" width="6" height="78" fill="var(--silver)"/><rect x="162" y="86" width="6" height="52" fill="var(--pink)"/>
    <g font-family="Roboto, sans-serif" font-size="4" fill="#999" text-anchor="middle"><text x="38" y="147">Category 1</text><text x="78" y="147">Category 2</text><text x="118" y="147">Category 3</text><text x="158" y="147">Category 4</text></g>
  </svg>
  <div class="a" style="left:248px;top:44px;font-size:5px;letter-spacing:2px;color:var(--gray)">LOREM IPSUM DOLOR</div>
  <div class="a h" style="left:248px;top:54px;font-size:16px;line-height:1.2">Company<br>Statistics</div>
  <div class="dot" style="left:252px;top:118px;width:14px;height:14px;border:1px solid var(--teal)"></div>
  <div class="a" style="left:274px;top:116px;width:100px"><div class="h" style="font-size:4.8px">Description here</div><p class="t">Our mission is delivering creative solution through visual</p></div>
  <div class="dot" style="left:252px;top:154px;width:14px;height:14px;border:1px solid var(--teal)"></div>
  <div class="a" style="left:274px;top:152px;width:100px"><div class="h" style="font-size:4.8px">Description here</div><p class="t">Our mission is delivering creative solution through visual</p></div>
  <div class="brand sm">dorneck-saalig</div><div class="page">PAGE | 30</div>
</section>

<!-- 28 bar chart labelled -->
<section class="slide">
  <div class="accent-line"></div>
  <svg class="a" style="left:20px;top:62px" width="170" height="130" viewBox="0 0 170 130">
    <line x1="0" y1="112" x2="170" y2="112" stroke="#ddd" stroke-width=".5"/>
    <rect x="22" y="16" width="12" height="96" fill="var(--teal)"/><rect x="58" y="70" width="12" height="42" fill="var(--pink)"/><rect x="94" y="46" width="12" height="66" fill="var(--silver)"/><rect x="130" y="100" width="12" height="12" fill="var(--gray)"/>
    <g font-family="Roboto, sans-serif" font-size="5" font-weight="700" fill="#fff" text-anchor="middle">
      <rect x="21" y="5" width="14" height="8" rx="1" fill="#e9e9e9"/><text x="28" y="11" fill="#555">80</text>
      <rect x="57" y="59" width="14" height="8" rx="1" fill="#e9e9e9"/><text x="64" y="65" fill="#555">35</text>
      <rect x="93" y="35" width="14" height="8" rx="1" fill="#e9e9e9"/><text x="100" y="41" fill="#555">55</text>
      <rect x="129" y="89" width="14" height="8" rx="1" fill="#e9e9e9"/><text x="136" y="95" fill="#555">10</text>
    </g>
    <g font-family="Roboto, sans-serif" font-size="4" fill="#999" text-anchor="middle"><text x="28" y="121">Category 1</text><text x="64" y="121">Category 2</text><text x="100" y="121">Category 3</text><text x="136" y="121">Category 4</text></g>
  </svg>
  <div class="bullet-row" style="left:212px;top:76px;width:160px;font-size:4.8px;line-height:1.35;color:var(--ink)"><i style="width:6px;height:6px"></i><span>Lorem ipsum dolor sit amet, quam id eros. Vestibulum luctus velit. Pretium ante, integer a blandit. Nullam nunc wisi, rutrum rhoncus. Libero commodo. Ut a.</span></div>
  <div class="bullet-row" style="left:212px;top:104px;width:160px;font-size:4.8px;line-height:1.35;color:var(--ink)"><i style="width:6px;height:6px"></i><span>Imperdiet in pulvinar. Tellus augue. Elit urna dignissim. Inceptos. Ligula augue, etiam sit, et vestibulum.</span></div>
  <div class="bullet-row" style="left:212px;top:126px;width:160px;font-size:4.8px;line-height:1.35;color:var(--ink)"><i style="width:6px;height:6px"></i><span>Dolor lacus gravida. Elit placerat risus, cursus orci, eget pulvinar, tortor donec massa. Enim hendrerit proin. Rutrum consectetuer qui, wisi est, vel ante.</span></div>
  <div class="brand sm">dorneck-saalig</div><div class="page">PAGE | 31</div>
</section>

<!-- 29 line chart -->
<section class="slide">
  <svg class="a" style="left:18px;top:56px" width="190" height="130" viewBox="0 0 190 130">
    <polyline fill="none" stroke="var(--teal)" stroke-width="1.4" points="4,100 18,70 32,92 46,40 60,108 74,28 88,96 102,80 116,40 130,98 144,30 158,70 172,100"/>
    <polyline fill="none" stroke="var(--pink)" stroke-width="1.4" points="4,80 18,96 32,48 46,72 60,20 74,86 88,74 102,104 116,20 130,62 144,90 158,58 172,80"/>
    <g font-family="Roboto, sans-serif" font-size="4" fill="#888"><text x="22" y="66">4.4</text><text x="6" y="108">2.4</text><text x="42" y="112">1.8</text><text x="70" y="40">5.7</text><text x="88" y="84">3.2</text><text x="102" y="114">1.2</text><text x="120" y="34">6.7</text><text x="124" y="92">2.4</text><text x="144" y="96">2.9</text><text x="154" y="40">5.6</text><text x="170" y="96">2.4</text></g>
    <g font-family="Roboto, sans-serif" font-size="3.6" fill="#999"><text x="0" y="128">2003  2004  2007  2008  2009  2010  2011  2012  2013  2014  2015  2016</text></g>
  </svg>
  <div class="a h" style="left:224px;top:72px;font-size:15px">Chart</div>
  <div class="a" style="left:224px;top:92px;font-size:6px;color:var(--gray)">Lorem ipsum dolor sit amet</div>
  <div class="a" style="left:226px;top:110px;width:150px;font-size:4.4px;line-height:1.4;color:var(--ink)">
    <p style="margin-bottom:5px">○ Lorem ipsum dolor sit amet, consectetur adipiscing elit, sed do eiusmod tempor incididunt ut labore et dolore magna aliqua.</p>
    <p>○ Lorem ipsum dolor sit amet, consectetur adipiscing elit. Lorem ipsum dolor sit amet, consectetur adipiscing elit, sed do eiusmod tempor incididunt ut labore et dolore magna aliqua.</p>
  </div>
</section>

<!-- 30 roadmap -->
<section class="slide">
  <svg class="fill" viewBox="0 0 396 223">
    <path d="M30 0V20C30 36 40 44 56 44H356C372 44 378 54 378 70V100C378 112 372 120 356 120H44C30 120 24 128 24 140V180C24 196 32 204 48 204H396" fill="none" stroke="#d8d8d8" stroke-width="1"/>
    <g fill="var(--pink)"><rect x="78" y="40" width="54" height="8" rx="4"/><rect x="256" y="40" width="54" height="8" rx="4"/><rect x="166" y="116" width="54" height="8" rx="4"/></g>
    <g fill="var(--teal)"><rect x="168" y="40" width="54" height="8" rx="4"/><rect x="76" y="116" width="54" height="8" rx="4"/><rect x="256" y="116" width="54" height="8" rx="4"/></g>
    <g font-family="Roboto, sans-serif" font-size="4.6" fill="#fff" font-weight="500"><text x="84" y="46">2016</text><text x="174" y="46">2016</text><text x="262" y="46">2017</text><text x="82" y="122">2018</text><text x="172" y="122">2019</text><text x="262" y="122">2020</text></g>
  </svg>
  <p class="a t" style="left:80px;top:54px;width:58px">Lorem Ipsum is simply dummy unknown printer took a galley of type and scrambled it to make.</p>
  <p class="a t" style="left:170px;top:54px;width:58px">Lorem Ipsum is simply dummy unknown printer took a galley of type and scrambled it to make.</p>
  <p class="a t" style="left:258px;top:54px;width:58px">Lorem Ipsum is simply dummy unknown printer took a galley of type and scrambled it to make.</p>
  <p class="a t" style="left:78px;top:130px;width:58px">Lorem Ipsum is simply dummy unknown printer took a galley of type and scrambled it to make.</p>
  <p class="a t" style="left:168px;top:130px;width:58px">Lorem Ipsum is simply dummy unknown printer took a galley of type and scrambled it to make.</p>
  <p class="a t" style="left:258px;top:130px;width:58px">Lorem Ipsum is simply dummy unknown printer took a galley of type and scrambled it to make.</p>
  <div class="brand sm">dorneck-saalig</div><div class="page">PAGE | 33</div>
</section>

<!-- 31 thank you card -->
<section class="slide">
  <div class="a" style="left:52px;top:18px;font-size:11px;font-weight:500;color:var(--ink)">dorneck-saalig</div>
  <div class="card" style="left:44px;top:40px;width:106px;height:162px"></div>
  <div class="a contact white" style="left:44px;top:44px;width:106px;height:24px;background:var(--teal);padding-left:12px">
    <svg width="8" height="8" viewBox="0 0 10 10"><circle cx="5" cy="5" r="4.3" fill="none" stroke="#fff"/><path d="M1 5H9M5 .7C2.5 3 2.5 7 5 9.3M5 .7C7.5 3 7.5 7 5 9.3" fill="none" stroke="#fff" stroke-width=".8"/></svg>www.dorneck-saalig.de</div>
  <div class="a contact" style="left:56px;top:82px;color:var(--ink);line-height:1.3"><svg width="8" height="10" viewBox="0 0 8 10"><path d="M4 10C1 6 .5 5 .5 3.6a3.5 3.5 0 0 1 7 0C7.5 5 7 6 4 10Z" fill="none" stroke="var(--teal)"/></svg><span>Lindenhofweg 7<br>D-85570 Kirchfeld</span></div>
  <div class="a" style="left:52px;top:104px;width:90px;height:.5px;background:#ddd"></div>
  <div class="a contact" style="left:56px;top:114px;color:var(--ink)"><svg width="8" height="8" viewBox="0 0 10 10"><path d="M2 .5 4 3 3 4.5C4 6.5 5 7 5.5 7L7 6 9.5 8 8 9.5C4 9.5 .5 6 .5 2Z" fill="var(--teal)"/></svg>(+49) 170 / 55 12 308</div>
  <div class="a" style="left:52px;top:132px;width:90px;height:.5px;background:#ddd"></div>
  <div class="a contact" style="left:56px;top:142px;color:var(--ink)"><svg width="9" height="7" viewBox="0 0 10 7"><rect width="10" height="7" fill="var(--teal)"/><path d="M0 0 5 4 10 0" fill="none" stroke="#fff" stroke-width=".8"/></svg>marlene@dorneck-saalig.de</div>
  <div class="a" style="left:80px;top:208px;width:9px;height:9px;background:var(--ink)"></div>
  <div class="a" style="left:93px;top:208px;width:9px;height:9px;background:var(--ink)"></div>
  <div class="a" style="left:210px;top:97px;font-size:22px;font-weight:900;color:#111">Thank You!</div>
</section>

<!-- 32 thank you photo -->
<section class="slide">
  <div class="a ph-table" style="inset:0" role="img" aria-label="Photo of a team working with laptops around a wooden table"></div>
  <svg class="fill" viewBox="0 0 396 223" preserveAspectRatio="none"><path d="M0 0H218C180 60 176 170 236 223H0Z" fill="var(--teal)"/></svg>
  <div class="a white" style="left:24px;top:22px;font-size:16px;font-weight:700">Thank You!</div>
  <div class="a contact white" style="left:30px;top:70px"><svg width="8" height="8" viewBox="0 0 10 10"><circle cx="5" cy="5" r="4.3" fill="none" stroke="#fff"/><path d="M1 5H9M5 .7C2.5 3 2.5 7 5 9.3M5 .7C7.5 3 7.5 7 5 9.3" fill="none" stroke="#fff" stroke-width=".8"/></svg>www.dorneck-saalig.de</div>
  <div class="a contact white" style="left:30px;top:92px"><svg width="8" height="10" viewBox="0 0 8 10"><path d="M4 10C1 6 .5 5 .5 3.6a3.5 3.5 0 0 1 7 0C7.5 5 7 6 4 10Z" fill="#fff"/></svg>Lindenhofweg 7, D-85570 Kirchfeld</div>
  <div class="a contact white" style="left:30px;top:114px"><svg width="8" height="8" viewBox="0 0 10 10"><path d="M2 .5 4 3 3 4.5C4 6.5 5 7 5.5 7L7 6 9.5 8 8 9.5C4 9.5 .5 6 .5 2Z" fill="#fff"/></svg>(+49) 170 / 55 12 308</div>
  <div class="a contact white" style="left:30px;top:136px"><svg width="9" height="7" viewBox="0 0 10 7"><rect width="10" height="7" fill="#fff"/><path d="M0 0 5 4 10 0" fill="none" stroke="var(--teal)" stroke-width=".8"/></svg>marlene@dorneck-saalig.de</div>
  <div class="brand" style="left:28px;top:196px">dorneck-saalig</div>
</section>

</main>
</body>
</html>
```